Oil and Gas Exploration and Production company needs a business card design

We need a business card design using our logo and colors in the logo. We want a mainstream design.

```html
<!DOCTYPE html>
<html lang="en">
<head>
<meta charset="utf-8">
<title>Quarra Oil &amp; Gas – Business Card</title>
<link href="https://fonts.googleapis.com/css2?family=Arimo:wght@400;700&display=swap" rel="stylesheet">
<style>
  :root {
    --gold: #d4a035;
    --black: #0b0b0b;
    --stage: #e9e7e3;
    --art-dark: #2a2216;
    --art-mid: #5e4820;
  }
  * { margin: 0; padding: 0; box-sizing: border-box; }
  html, body {
    width: 1200px;
    height: 902px;
    overflow: hidden;
    background: var(--stage);
    font-family: "Arimo", Arial, sans-serif;
  }
  .business-card {
    position: absolute;
    left: 120px;
    top: 177px;
    width: 960px;
    height: 548px;
    background: var(--gold);
    overflow: hidden;
    box-shadow: 0 12px 30px rgba(0,0,0,0.25);
  }
  .tagline {
    position: absolute;
    left: 34px;
    top: 36px;
    font-size: 30px;
    font-weight: 400;
    line-height: 1;
    color: var(--black);
  }
  .top-rule {
    position: absolute;
    left: 0;
    right: 0;
    top: 84px;
    height: 6px;
    background: var(--black);
  }
  .top-rule-accent {
    position: absolute;
    left: 640px;
    top: 0;
    width: 110px;
    height: 56px;
    background: var(--black);
  }
  .pumpjack-art {
    position: absolute;
    left: 150px;
    top: 140px;
    width: 340px;
    height: 210px;
    background: linear-gradient(180deg, var(--art-dark) 0%, var(--art-mid) 100%);
  }
  .bottom-band {
    position: absolute;
    left: 0;
    right: 0;
    top: 350px;
    bottom: 0;
    background: var(--black);
  }
  .brand {
    position: absolute;
    left: 520px;
    top: 256px;
    display: flex;
    align-items: center;
    gap: 16px;
  }
  .brand-dot {
    width: 46px;
    height: 46px;
    border-radius: 50%;
    background: var(--black);
    flex: none;
  }
  .brand-name {
    font-size: 92px;
    font-weight: 700;
    line-height: 1;
    color: var(--black);
  }
  .brand-sector {
    position: absolute;
    left: 582px;
    top: 372px;
    font-size: 50px;
    font-weight: 700;
    line-height: 1;
    color: var(--gold);
    letter-spacing: 8px;
  }
</style>
</head>
<body>
  <div class="business-card">
    <p class="tagline">Exploration and Production company</p>
    <div class="top-rule-accent"></div>
    <div class="top-rule"></div>

    <div class="pumpjack-art" role="img" aria-label="Silhouette illustration of an oil pumpjack"></div>

    <div class="bottom-band"></div>

    <div class="brand">
      <span class="brand-dot"></span>
      <span class="brand-name">Quarra</span>
    </div>
    <p class="brand-sector">OIL &amp; GAS</p>
  </div>
</body>
</html>
```